Re-brand our business and design!

We need a simple informational website (editable for in the future use)
We need our logo(we have included logo), name, who we are, and what we do displayed.

This is our current site (which is not acceptable, and only a template site): all our information is on this site, please use it forreferanceofinformation.
Www.brightlanefixers.com

Target Market(s)

Real estate brokers, and realtors,homeowners, and anyone looking for home repairs.

Industry/Entity Type

Business

Number of Pages Required

4 page

Font styles to use
Sans Serif

Requirements
Must have
• Our name, contact info, services, and our logo (which we will Email upon request)
• MUST have originality to the site.
• custom "contact us form" or request an estimate form.
Nice to have
• page for real customer testimonies.
• page for our previous work where we can upload pics of completed jobs.
Should not have
• any infringements on any copyrights or plagiarism at all.

```html
<!DOCTYPE html>
<html lang="en">
<head>
<meta charset="utf-8">
<title>Bright Lane Fixers And Maintenance</title>
<link rel="stylesheet" href="https://fonts.googleapis.com/css2?family=Open+Sans:ital,wght@0,400;0,600;0,700;1,400&family=Alegreya:wght@500&display=swap">
<style>
:root{
  --red:#d8141b;
  --ink:#1c1c1c;
  --grey:#6f6f6f;
  --muted:#8a8a8a;
  --line:#bdbdbd;
  --white:#ffffff;
  --topbar:#0d0d0d;
  --footer:#1e1e22;
  --navy:#23243a;
  --brown:#3a2a1e;
  --panel:#f1f1f1;
}
*{box-sizing:border-box;margin:0;padding:0}
html,body{width:1200px;height:3147px;overflow:hidden}
body{position:relative;font-family:"Open Sans",Arial,sans-serif;color:var(--ink);background:var(--white)}
.abs{position:absolute}
a{color:inherit;text-decoration:none}

/* top bar */
.topbar{left:0;top:0;width:1200px;height:46px;background:var(--topbar)}
.estimate-btn{left:80px;top:0;width:224px;height:46px;background:var(--red);color:var(--white);font-size:15px;font-weight:700;display:flex;align-items:center;gap:14px;padding-left:18px}
.phone-box{left:938px;top:0;width:262px;height:46px;display:flex;align-items:center;color:var(--white);font-size:19px;font-weight:600}
.phone-box .icon{width:48px;height:46px;background:var(--red);display:flex;align-items:center;justify-content:center;margin-right:18px}

/* nav */
.nav{left:0;top:46px;width:1200px;height:118px;background:var(--white);border-bottom:1px solid #e3e3e3}
.nav-link{top:96px;font-size:18px;font-weight:600;color:var(--ink)}
.nav-sep{top:94px;width:1px;height:24px;background:#cfcfcf}
.brand{left:430px;top:96px;width:340px;text-align:center;color:var(--ink);font-weight:700;line-height:1.15}
.brand .name{font-size:27px;display:block}
.brand .sub{font-size:17px;display:block;color:#555}

/* hero */
.hero{left:0;top:164px;width:1200px;height:470px;background:linear-gradient(90deg,#6d7d92 0%,#9aa4b0 35%,#7b7b7b 65%,#3b3b3b 100%)}
.hero-title{right:84px;top:356px;text-align:right;font-family:"Alegreya",Georgia,serif;font-weight:500;font-size:40px;line-height:52px;color:var(--white)}
.hero-sub{right:84px;top:478px;font-size:29px;font-weight:600;color:var(--white)}

/* section titles */
.sec-title{left:0;width:1200px;text-align:center;font-size:28px;font-weight:700}
.sec-title .soft{color:var(--muted);font-weight:600}
.divider{height:2px;background:var(--line)}
.divider.light{background:rgba(255,255,255,.55)}

/* welcome */
.welcome-text{left:88px;top:764px;width:1024px;text-align:center;font-size:14px;line-height:26px;color:#3a3a3a}
.read-more{left:596px;top:904px;width:110px;height:32px;background:var(--red);color:var(--white);font-size:14px;font-weight:600;display:flex;align-items:center;justify-content:center}
.read-more-bar{left:503px;top:934px;width:93px;height:2px;background:#555}

/* services */
.services{left:0;top:982px;width:1200px;height:476px;background:linear-gradient(120deg,#241a12 0%,#4a3726 45%,#2c2016 75%,#5b4330 100%)}
.hub{left:400px;top:1255px;width:400px;height:203px;background:var(--white);border-radius:200px 200px 0 0}
.hub-brand{left:400px;top:1372px;width:400px;text-align:center;font-weight:700;color:var(--ink);line-height:1.2}
.hub-brand .name{font-size:24px;display:block}
.hub-brand .sub{font-size:15px;display:block;color:#555}
.svc-icon{width:76px;height:76px;border-radius:50%;background:var(--red);border:3px solid var(--white);display:flex;align-items:center;justify-content:center}
.svc{color:var(--white);width:300px}
.svc h3{font-size:19px;font-weight:700;line-height:26px}
.svc p{font-size:13px;line-height:20px;color:#e6e6e6}
.svc.left{text-align:right}

/* projects */
.tile{border-radius:2px}
.slider-arrow{top:1730px}
.video-bar{left:80px;top:1874px;width:310px;height:35px;background:#111}

/* testimonials */
.testimonials{left:0;top:1962px;width:1200px;height:381px;background:linear-gradient(180deg,#2a2b40 0%,#1d1e30 100%)}
.quote{left:170px;top:2096px;width:860px;text-align:center;font-style:italic;font-size:15px;line-height:28px;color:#e8e8ee}
.quote-mark{font-family:Georgia,serif;font-size:40px;color:#8a8ba0}
.avatar{left:525px;top:2165px;width:100px;height:100px;border-radius:50%;border:4px solid var(--white);background:linear-gradient(160deg,#c89a80,#7a4a36)}
.dot{top:2283px;width:9px;height:9px;border-radius:50%;background:#9a9aa8}

/* map */
.map{left:0;top:2343px;width:1200px;height:378px;background:linear-gradient(135deg,#e6e4dc 0%,#d9dccf 50%,#e8e3d6 100%)}
.map-tag{left:535px;top:2427px;width:174px;height:59px;background:var(--white);box-shadow:0 2px 6px rgba(0,0,0,.25);display:flex;align-items:center;justify-content:center;font-size:15px;font-weight:700;text-align:center;line-height:1.15}

/* contact */
.contact{left:0;top:2721px;width:1200px;height:363px;background:var(--panel)}
.contact-lead{left:99px;top:2836px;font-size:17px;color:#333}
.field{background:var(--white);border:1px solid #d4d4d4;font-size:12px;color:#333;padding:0 10px;display:flex;align-items:center}
.field.area{align-items:flex-start;padding-top:12px}
.submit{left:371px;top:2994px;width:103px;height:38px;background:var(--red);color:var(--white);font-size:17px;font-weight:700;display:flex;align-items:center;justify-content:center}
.contact-col{left:790px;top:2790px;width:1px;height:270px;background:#d4d4d4}
.info h4{font-size:16px;font-weight:700;line-height:22px}
.info p{font-size:12px;line-height:18px;color:#333}
.info .strong{font-weight:700}
.info .big{font-size:19px;line-height:26px}

/* footer */
.footer{left:0;top:3084px;width:1200px;height:63px;background:var(--footer)}
.copy{left:99px;top:3105px;font-size:13px;font-weight:600;color:var(--white)}
.social{top:3098px;width:34px;height:34px;border-radius:50%;border:2px solid #555}
</style>
</head>
<body>

<!-- top bar -->
<div class="abs topbar"></div>
<a class="abs estimate-btn" href="#estimate">
  <svg width="22" height="22" viewBox="0 0 22 22" aria-hidden="true"><rect x="2" y="4" width="18" height="16" rx="2" fill="none" stroke="#fff" stroke-width="2"/><line x1="2" y1="9" x2="20" y2="9" stroke="#fff" stroke-width="2"/><line x1="7" y1="1" x2="7" y2="6" stroke="#fff" stroke-width="2"/><line x1="15" y1="1" x2="15" y2="6" stroke="#fff" stroke-width="2"/></svg>
  Request An Estimate
</a>
<div class="abs phone-box">
  <span class="icon"><svg width="20" height="20" viewBox="0 0 24 24" aria-hidden="true"><path d="M6.6 10.8c1.4 2.8 3.8 5.1 6.6 6.6l2.2-2.2c.3-.3.7-.4 1-.2 1.1.4 2.3.6 3.6.6.6 0 1 .4 1 1V20c0 .6-.4 1-1 1C10.6 21 3 13.4 3 4c0-.6.4-1 1-1h3.5c.6 0 1 .4 1 1 0 1.3.2 2.5.6 3.6.1.3 0 .7-.2 1z" fill="#fff"/></svg></span>
  555-014-2290
</div>

<!-- navigation -->
<div class="abs nav"></div>
<a class="abs nav-link" style="left:86px" href="#">Home</a>
<span class="abs nav-sep" style="left:164px"></span>
<a class="abs nav-link" style="left:192px" href="#">About</a>
<span class="abs nav-sep" style="left:270px"></span>
<a class="abs nav-link" style="left:299px" href="#">Services</a>
<div class="abs brand"><span class="name">Bright Lane Fixers</span><span class="sub">And Maintenance</span></div>
<a class="abs nav-link" style="left:877px" href="#">Projects</a>
<span class="abs nav-sep" style="left:988px"></span>
<a class="abs nav-link" style="left:1017px" href="#">Contact Us</a>

<!-- hero -->
<div class="abs hero" role="img" aria-label="Photo of a smiling plumber holding a wrench under a kitchen sink"></div>
<h1 class="abs hero-title">An Inspection Reveal Repairs<br>Needed Before Closing?</h1>
<p class="abs hero-sub">Bright Lane Fixers Can Help!</p>

<!-- welcome -->
<h2 class="abs sec-title" style="top:674px">Welcome To Bright Lane Fixers <span class="soft">And Maintenance</span></h2>
<div class="abs divider" style="left:238px;top:735px;width:724px"></div>
<p class="abs welcome-text">Lorem ipsum dolor sit amet, consectetuer adipiscing elit, sed diam nonummy nibh euismod tincidunt ut laoreet dolore magna aliquam erat volutpat. Ut wisi enim ad minim veniam, quis nostrud exerci tation ullamcorper suscipit lobortis nisl ut aliquip ex ea commodo consequat. Duis autem vel eum iriure dolor in hendrerit in vulputate velit esse molestie consequat, vel illum dolore eu feugiat nulla facilisis at vero eros et accumsan et iusto odio dignissim qui blandit praesent luptatum zzril delenit augue duis dolore te feugait nulla facilisi.</p>
<div class="abs read-more-bar"></div>
<a class="abs read-more" href="#">Read More</a>

<!-- services -->
<div class="abs services" role="img" aria-label="Dark wooden workbench with hand tools and a hammer"></div>
<h2 class="abs sec-title" style="top:1022px;color:var(--white);font-size:27px">Our Services</h2>
<div class="abs divider light" style="left:496px;top:1080px;width:208px"></div>

<svg class="abs" style="left:300px;top:1170px" width="600" height="290" viewBox="0 0 600 290" aria-hidden="true">
  <g stroke="#fff" stroke-width="2" fill="none">
    <line x1="210" y1="43" x2="228" y2="88"/>
    <line x1="369" y1="43" x2="372" y2="88"/>
    <line x1="137" y1="106" x2="170" y2="146"/>
    <line x1="455" y1="106" x2="430" y2="146"/>
    <line x1="63" y1="210" x2="110" y2="234"/>
    <line x1="518" y1="210" x2="490" y2="234"/>
  </g>
  <g fill="#d8141b" stroke="#fff" stroke-width="2">
    <circle cx="228" cy="88" r="7"/><circle cx="372" cy="88" r="7"/>
    <circle cx="170" cy="146" r="7"/><circle cx="430" cy="146" r="7"/>
    <circle cx="110" cy="234" r="7"/><circle cx="490" cy="234" r="7"/>
  </g>
</svg>

<div class="abs hub"></div>
<div class="abs hub-brand"><span class="name">Bright Lane Fixers</span><span class="sub">And Maintenance</span></div>

<!-- carpentry -->
<div class="abs svc-icon" style="left:472px;top:1137px"><svg width="34" height="34" viewBox="0 0 34 34" aria-hidden="true"><rect x="5" y="14" width="24" height="5" fill="#fff"/><rect x="8" y="19" width="3" height="11" fill="#fff"/><rect x="23" y="19" width="3" height="11" fill="#fff"/><rect x="14" y="4" width="6" height="10" fill="#fff"/></svg></div>
<div class="abs svc left" style="left:157px;top:1140px"><h3>Carpentry</h3><p>Stairs, Floors, Decks, Fences<br>Storage sheds, Storage shelving</p></div>
<!-- electrical -->
<div class="abs svc-icon" style="left:631px;top:1137px"><svg width="34" height="34" viewBox="0 0 34 34" aria-hidden="true"><circle cx="17" cy="17" r="13" fill="none" stroke="#fff" stroke-width="2.5"/><path d="M19 7l-8 12h6l-2 9 8-12h-6z" fill="#fff"/></svg></div>
<div class="abs svc" style="left:729px;top:1140px"><h3>Electrical</h3><p>Bathrooms, Kitchens, Washer/Dryer<br>Hook Up Clogged drains, Toilets</p></div>
<!-- plumbing -->
<div class="abs svc-icon" style="left:361px;top:1223px"><svg width="34" height="34" viewBox="0 0 34 34" aria-hidden="true"><path d="M4 12h14v6h8v12h-6v-6h-8v-6H4z" fill="#fff"/><rect x="8" y="6" width="6" height="6" fill="#fff"/></svg></div>
<div class="abs svc left" style="left:29px;top:1226px"><h3>Plumbing</h3><p>Bathrooms, Kitchens, Washer/Dryer<br>Hook Up Clogged drains, Toilets</p></div>
<!-- small construction -->
<div class="abs svc-icon" style="left:755px;top:1223px"><svg width="34" height="34" viewBox="0 0 34 34" aria-hidden="true"><line x1="7" y1="27" x2="25" y2="9" stroke="#fff" stroke-width="4" stroke-linecap="round"/><line x1="9" y1="9" x2="27" y2="27" stroke="#fff" stroke-width="4" stroke-linecap="round"/></svg></div>
<div class="abs svc" style="left:850px;top:1226px"><h3>Small Construction</h3><p>Painting, Pressure/Power washing<br>Heavy lifting, Property Clean Outs</p></div>
<!-- doors & windows -->
<div class="abs svc-icon" style="left:287px;top:1342px"><svg width="34" height="34" viewBox="0 0 34 34" aria-hidden="true"><rect x="6" y="6" width="22" height="22" fill="none" stroke="#fff" stroke-width="2.5"/><line x1="17" y1="6" x2="17" y2="28" stroke="#fff" stroke-width="2.5"/><line x1="6" y1="17" x2="28" y2="17" stroke="#fff" stroke-width="2.5"/></svg></div>
<div class="abs svc left" style="left:-30px;top:1343px"><h3>Doors &amp; Windows</h3><p>Weatherstripping,<br>Replacements Glass and</p></div>
<!-- roofing -->
<div class="abs svc-icon" style="left:818px;top:1342px"><svg width="34" height="34" viewBox="0 0 34 34" aria-hidden="true"><path d="M3 18L17 6l14 12" fill="none" stroke="#fff" stroke-width="3"/><rect x="9" y="18" width="16" height="11" fill="#fff"/></svg></div>
<div class="abs svc" style="left:910px;top:1343px"><h3>Roofing Maintenance</h3><p>Painting, Pressure/Power<br>washing Heavy lifting, Property</p></div>

<!-- projects -->
<h2 class="abs sec-title" style="top:1496px;font-size:27px">Project <span class="soft">Showcase</span></h2>
<div class="abs divider" style="left:464px;top:1552px;width:272px"></div>

<svg class="abs slider-arrow" style="left:28px" width="20" height="40" viewBox="0 0 20 40" aria-hidden="true"><polyline points="17,2 3,20 17,38" fill="none" stroke="#444" stroke-width="2"/></svg>
<svg class="abs slider-arrow" style="left:1148px" width="20" height="40" viewBox="0 0 20 40" aria-hidden="true"><polyline points="3,2 17,20 3,38" fill="none" stroke="#444" stroke-width="2"/></svg>

<div class="abs tile" style="left:80px;top:1605px;width:310px;height:269px;background:linear-gradient(160deg,#5a6a54,#8c8e86 50%,#3e4a3a)" role="img" aria-label="Video still of two workers installing a front door"></div>
<div class="abs video-bar"></div>
<svg class="abs" style="left:80px;top:1874px" width="310" height="35" viewBox="0 0 310 35" aria-hidden="true"><polygon points="14,11 14,24 24,17.5" fill="#fff"/><rect x="38" y="13" width="8" height="9" fill="#fff"/><rect x="66" y="16" width="150" height="3" fill="#2d7fd1"/><rect x="216" y="16" width="80" height="3" fill="#555"/></svg>
<svg class="abs" style="left:209px;top:1714px" width="52" height="52" viewBox="0 0 52 52" aria-hidden="true"><circle cx="26" cy="26" r="24" fill="rgba(0,0,0,.45)" stroke="#fff" stroke-width="2"/><polygon points="21,16 21,36 37,26" fill="#fff"/></svg>

<div class="abs tile" style="left:403px;top:1605px;width:195px;height:147px;background:linear-gradient(150deg,#e9d7c0,#c69a6c)" role="img" aria-label="Hands marking a timber board with a pencil"></div>
<div class="abs tile" style="left:403px;top:1769px;width:195px;height:140px;background:linear-gradient(150deg,#c5ccd6,#5a6a86)" role="img" aria-label="Plumber repairing pipes under a sink"></div>
<div class="abs tile" style="left:615px;top:1605px;width:287px;height:128px;background:linear-gradient(150deg,#d8d4cc,#9d968a)" role="img" aria-label="Empty renovated room with tall windows"></div>
<div class="abs tile" style="left:615px;top:1746px;width:287px;height:163px;background:linear-gradient(150deg,#d1a878,#8a6036)" role="img" aria-label="Drilling into a wooden plank"></div>
<div class="abs tile" style="left:917px;top:1605px;width:203px;height:304px;background:linear-gradient(150deg,#e6c49a,#b07a48)" role="img" aria-label="Carpenter measuring wood with a ruler"></div>

<!-- testimonials -->
<div class="abs testimonials" role="img" aria-label="Dim photo of a hand writing with a pen"></div>
<h2 class="abs sec-title" style="top:1998px;color:var(--white);font-size:26px;font-weight:600">Client Testimonials</h2>
<div class="abs divider light" style="left:446px;top:2050px;width:308px"></div>
<span class="abs quote-mark" style="left:146px;top:2080px">“</span>
<p class="abs quote">Lorem ipsum dolor sit amet,ffg jnfkvjbnig consectetuer adipiscing elit, sed diamggi. nonummy nibh euismod tincidunt uthjh elit.<br>laoreet dolore magna aliquam eratghs consectetuer adipiscing elit. Lorem ipsum donor</p>
<span class="abs quote-mark" style="left:934px;top:2122px">”</span>
<div class="abs avatar" role="img" aria-label="Portrait of a client"></div>
<span class="abs dot" style="left:556px"></span>
<span class="abs dot" style="left:571px;background:var(--red)"></span>
<span class="abs dot" style="left:586px"></span>

<!-- map -->
<div class="abs map" role="img" aria-label="Street map of the service area"></div>
<div class="abs map-tag">Bright Lane Fixers<br>And Maintenance</div>

<!-- contact -->
<div class="abs contact"></div>
<h2 class="abs sec-title" style="top:2745px;font-size:27px">Contact <span class="soft">Us</span></h2>
<div class="abs divider" style="left:524px;top:2796px;width:152px"></div>
<p class="abs contact-lead">Please Fill Your Details We will Get Back to You Soon</p>
<div class="abs field" style="left:92px;top:2885px;width:256px;height:37px">Name</div>
<div class="abs field" style="left:92px;top:2941px;width:256px;height:38px">Email</div>
<div class="abs field" style="left:92px;top:2994px;width:256px;height:38px">Phone</div>
<div class="abs field area" style="left:371px;top:2885px;width:342px;height:90px">How We Can Help You?</div>
<div class="abs submit">Submit</div>
<div class="abs contact-col"></div>

<svg class="abs" style="left:816px;top:2822px" width="16" height="20" viewBox="0 0 16 20" aria-hidden="true"><path d="M8 0C3.6 0 0 3.4 0 7.6 0 13 8 20 8 20s8-7 8-12.4C16 3.4 12.4 0 8 0z" fill="#d8141b"/><circle cx="8" cy="7.5" r="3" fill="#fff"/></svg>
<div class="abs info" style="left:850px;top:2821px;width:330px">
  <h4>ADDRESS</h4>
  <p class="strong">Bright Lane Fixers And Maintenance</p>
  <p>123, Lorewam Dollar almet sit , Smit<br>Amet - 123456</p>
</div>
<svg class="abs" style="left:814px;top:2926px" width="20" height="14" viewBox="0 0 20 14" aria-hidden="true"><rect width="20" height="14" fill="#d8141b"/><polyline points="1,1 10,8 19,1" fill="none" stroke="#fff" stroke-width="1.6"/></svg>
<div class="abs info" style="left:850px;top:2922px;width:330px">
  <h4>EMAIL</h4>
  <p>Www.brightlanefixers.com</p>
</div>
<svg class="abs" style="left:815px;top:2995px" width="18" height="18" viewBox="0 0 24 24" aria-hidden="true"><path d="M6.6 10.8c1.4 2.8 3.8 5.1 6.6 6.6l2.2-2.2c.3-.3.7-.4 1-.2 1.1.4 2.3.6 3.6.6.6 0 1 .4 1 1V20c0 .6-.4 1-1 1C10.6 21 3 13.4 3 4c0-.6.4-1 1-1h3.5c.6 0 1 .4 1 1 0 1.3.2 2.5.6 3.6.1.3 0 .7-.2 1z" fill="#d8141b"/></svg>
<div class="abs info" style="left:850px;top:2993px;width:330px">
  <h4>CALL US</h4>
  <p class="big">555-014-2290</p>
</div>

<!-- footer -->
<div class="abs footer"></div>
<p class="abs copy">Copyright © 2016 Bright Lane Fixers And Maintenance.  All Rights Reserved.</p>
<span class="abs social" style="left:845px;background:#3b5998"></span>
<span class="abs social" style="left:891px;background:#0e76a8"></span>
<span class="abs social" style="left:935px;background:#1da1f2"></span>
<span class="abs social" style="left:982px;background:#dd4b39"></span>

</body>
</html>
```